" Somos especializados em blockchains para grandes empresas. Nossa diferença é possibilitar que as diferentes blockchains de uma empresa possam se comunicar entre si. O termo Corval (parte do nosso nome Corvalink) foi popularizado no livro, escrito por Theodore Brannick, A Curva do Silêncio. Corvals são as pessoas que possuem uma rede de conhecidos que confiam um no outro; normalmente é uma rede que vai através de diversas barreiras sociais e grupos. Hoje as blockchains são redes isoladas. Por exemplo, se você criar sua própria blockchain, com a finalidade de ter uma rede de rastreamento para sua cadeia de suprimentos, teoricamente, não poderá usar a mesma para fazer pagamentos (ex. lumerix), tendo assim, que criar uma segunda blockchain. A corvalink oferece a tecnologia que possibilita a criação de uma blockchain que se comunica com outras blockchains, sem perder a descentralização. Basicamente, isso permite criar uma internet de blockchain. "

```html
<!DOCTYPE html>
<html lang="pt-BR">
<head>
<meta charset="utf-8">
<title>Corvalink — Modelo de Slide</title>
<link rel="stylesheet" href="https://fonts.googleapis.com/css2?family=Fira+Sans:ital,wght@0,400;0,700;1,400;1,700;1,800&display=swap">
<style>
  :root {
    --page-bg: #e9e9ec;
    --slide-bg: #ffffff;
    --slide-fade: #eeeef1;
    --purple: #5b2a86;
    --purple-deep: #4a1f70;
    --gray-title: #6d6e71;
    --gray-text: #55565a;
    --gray-line: #c9c9cc;
    --gray-foot: #8a8b8e;
  }
  * { box-sizing: border-box; margin: 0; padding: 0; }
  html, body {
    width: 1200px; height: 1200px; overflow: hidden;
    background: var(--page-bg);
    font-family: "Fira Sans", "Helvetica Neue", Arial, sans-serif;
  }
  .stage {
    width: 1200px; height: 1200px;
    display: flex; align-items: center; justify-content: center;
  }
  .slide {
    position: relative;
    width: 1100px; height: 825px;
    background: linear-gradient(180deg, var(--slide-bg) 0%, var(--slide-bg) 70%, var(--slide-fade) 100%);
    box-shadow: 0 6px 24px rgba(0,0,0,0.12);
  }
  .slide-header {
    position: absolute; left: 0; right: 0; top: 0; height: 120px;
  }
  .brand-name {
    position: absolute; left: 60px; top: 70px;
    display: flex; align-items: center; gap: 10px;
    font-weight: 700; font-size: 20px; letter-spacing: 2px;
    color: var(--purple);
  }
  .brand-square {
    width: 22px; height: 22px; background: var(--purple);
  }
  .presentation-title {
    position: absolute; right: 70px; top: 30px;
    font-weight: 800; font-style: italic; font-size: 40px;
    color: var(--purple); letter-spacing: 0.5px;
  }
  .header-rule {
    position: absolute; left: 0; right: 0; top: 104px; height: 3px;
    background: linear-gradient(90deg, var(--gray-line) 0%, var(--gray-line) 22%, var(--purple) 22%, var(--purple) 100%);
  }
  .slide-body {
    position: absolute; left: 90px; right: 90px; top: 150px;
  }
  .slide-title {
    font-weight: 800; font-style: italic; font-size: 32px;
    color: var(--gray-title); line-height: 1.05;
  }
  .slide-subtitle {
    font-weight: 700; font-style: italic; font-size: 27px;
    color: var(--purple); line-height: 1.1; margin-bottom: 18px;
  }
  .slide-text {
    font-size: 20px; line-height: 1.5; color: var(--gray-text);
    text-align: justify; text-indent: 40px;
  }
  .slide-text + .slide-text { margin-top: 4px; font-style: italic; }
  .slide-text strong { color: #3d3e42; }
  .footer-brand {
    position: absolute; right: 70px; bottom: 120px;
    font-weight: 700; font-size: 18px; letter-spacing: 2px;
    color: var(--purple);
  }
  .footer-rule {
    position: absolute; left: 0; right: 0; bottom: 90px; height: 3px;
    background: var(--purple);
  }
  .footer-site {
    position: absolute; right: 60px; bottom: 40px;
    font-style: italic; font-size: 24px; color: var(--gray-foot);
  }
</style>
</head>
<body>
<main class="stage">
  <section class="slide">
    <header class="slide-header">
      <div class="brand-name"><span class="brand-square"></span>CORVALINK</div>
      <h1 class="presentation-title">TÍTULO DA APRESENTAÇÃO</h1>
      <div class="header-rule"></div>
    </header>

    <article class="slide-body">
      <h2 class="slide-title">TÍTULO DO SLIDE</h2>
      <h3 class="slide-subtitle">Subtítulo</h3>
      <p class="slide-text">Sed ut perspiciatis unde omnis iste natus error sit voluptatem accusantium doloremque <strong>laudantium, totam rem aperiam, eaque ipsa quae ab illo inventore veritatis</strong> et quasi architecto beatae vitae dicta sunt explicabo. Nemo enim ipsam voluptatem quia voluptas sit aspernatur aut odit aut fugit, sed quia consequuntur magni dolores eos qui ratione voluptatem sequi nesciunt. Neque porro quisquam est, qui dolorem ipsum quia dolor sit amet, consectetur, adipisci velit, sed quia non numquam eius modi tempora incidunt ut labore et dolore magnam aliquam quaerat voluptatem.</p>
      <p class="slide-text">Ut enim ad minima veniam, quis nostrum exercitationem ullam corporis suscipit laboriosam, nisi ut aliquid ex ea commodi consequatur? Quis autem vel eum iure reprehenderit qui in ea voluptate velit esse quam nihil molestiae consequatur, vel illum qui dolorem eum fugiat quo voluptas nulla pariatur?”</p>
    </article>

    <div class="footer-brand">CORVALINK</div>
    <div class="footer-rule"></div>
    <div class="footer-site">www.suapagina.com.br</div>
  </section>
</main>
</body>
</html>
```